"Landing Page Design for Premium Eco-Friendly Laundry Strips – Plooifris.nl"

We need a visually appealing and high-converting landing page for our premium laundry strips, emphasizing luxury, sustainability, and ease of use. The page should include sections such as:

Hero Section: A compelling introduction with a strong headline, subheadline, and a clear call-to-action (CTA).
Product Benefits: Highlighting key features like eco-friendliness, long-lasting scent, and hypoallergenic qualities.
Product Description: Focusing on innovation and sustainability.
How It Works: Simple, visual steps for using the product.
Customer Reviews: Authentic testimonials to build trust and social proof.
FAQ Section: Addressing common concerns about the product.
The design should maintain a luxurious aesthetic while ensuring clarity and user-friendliness. We also offer free shipping on all orders, a key differentiator to be prominently displayed. All texts and translations are already provided for implementation. Please deliver the design in Figma format."

Target Market(s)

"Eco-conscious consumers and families seeking premium and sustainable laundry solutions. Target age group: 25-50, predominantly women who prioritize luxury and environmental impact."

Industry/Entity Type

"Laundry care and eco-friendly consumer goods."

Coding

Requirements
Must have
• A visually luxurious design emphasizing premium quality and eco-friendliness. Clear call-to-actions (e.g., 'Try Now – Free Shipping'). Sections for product benefits, how it works, customer reviews, and FAQ. Highlight free shipping with no minimum order prominently."
Nice to have
• Elegant, minimalist animations to enhance the premium feel. Subtle use of gold and black to emphasize luxury, with a touch of green for sustainability. Interactive customer reviews section (e.g., carousel or testimonials)."
Should not have
• Overly cluttered designs or overwhelming text blocks. Generic stock photos not aligned with our brand identity. Bright or overly playful color schemes that detract from the premium feel."

```html
<!DOCTYPE html>
<html lang="en">
<head>
<meta charset="utf-8">
<title>Plooifris – Premium Laundry Strips</title>
<link href="https://fonts.googleapis.com/css2?family=Jost:wght@400;500;600&family=Inter:wght@400;500&display=swap" rel="stylesheet">
<style>
:root{
  --gold:#d9a531;
  --gold-light:#ecc56a;
  --gold-deep:#b8861f;
  --black:#050505;
  --white:#ffffff;
  --cream:#f6e7bd;
  --text:#222222;
  --muted:#555555;
}
*{box-sizing:border-box;margin:0;padding:0}
html,body{width:1200px;height:4019px;overflow:hidden;background:var(--white)}
body{font-family:"Inter",Arial,sans-serif;color:var(--text)}
.page{position:relative;width:1200px;height:4019px;overflow:hidden}
.backdrop{position:absolute;left:0;top:0;width:1200px;height:4019px}
.abs{position:absolute}
.center{left:0;width:1200px;text-align:center}
h1,h2,h3{font-family:"Jost",sans-serif;font-weight:500}

/* nav */
.brand{position:absolute;left:84px;top:12px;width:130px;text-align:center}
.brand-dot{width:54px;height:54px;border-radius:50%;background:var(--gold);margin:0 auto 24px}
.brand-name{font-family:"Jost",sans-serif;font-weight:500;font-size:15px;letter-spacing:1.5px;color:var(--gold)}
.nav{position:absolute;top:36px;left:468px;font-family:"Jost",sans-serif;font-size:13px;font-weight:500}
.nav a{color:var(--black);text-decoration:none;position:absolute;white-space:nowrap}
.nav a.active{color:var(--gold)}
.nav-tools{position:absolute;top:34px;left:1015px;display:flex;align-items:center;gap:14px;font-family:"Jost",sans-serif;font-size:13px}

/* buttons */
.btn{position:absolute;display:flex;align-items:center;justify-content:center;border-radius:4px;
  background:linear-gradient(180deg,var(--gold-light),var(--gold-deep));color:var(--white);
  font-family:"Jost",sans-serif;font-weight:600;font-size:10.5px;text-decoration:none}

/* hero */
.hero-title{top:110px;font-size:40px;line-height:46px;color:var(--black)}
.hero-sub{top:214px;font-size:12px;color:#444}

.box-art{position:absolute;border-radius:4px}

/* benefits */
.section-title-gold{color:var(--gold);font-size:37px;font-weight:600}
.benefit{position:absolute;width:250px;text-align:center;color:var(--white)}
.benefit svg{display:block;margin:0 auto 8px}
.benefit h3{font-size:18px;color:var(--gold);font-weight:600;margin-bottom:3px}
.benefit p{font-size:12px;line-height:15px;color:#e8e8e8}

/* future */
.future-title{left:686px;top:1718px;font-size:40px;line-height:46px;color:var(--black)}
.future-text{left:686px;top:1822px;width:362px;font-size:12px;line-height:18.7px;color:#333}

/* steps */
.steps-title{top:2048px;font-size:37px;color:var(--black)}
.step{position:absolute;width:200px;text-align:center}
.step .num{font-family:"Jost",sans-serif;font-weight:600;font-size:44px;color:var(--gold);line-height:44px}
.step p{font-size:12px;line-height:18px;color:#333;margin-top:10px}

/* faq */
.faq-title{top:2640px;font-size:37px;color:var(--white);font-weight:600}
.faq-item{position:absolute;left:292px;width:605px;border:1.5px solid var(--gold);border-radius:3px;padding:0 36px;color:var(--white)}
.faq-q{display:flex;justify-content:space-between;font-family:"Jost",sans-serif;font-size:14px;color:var(--gold);font-weight:500}
.faq-a{font-size:11.5px;line-height:18px;margin-top:6px;color:#f1f1f1}

/* reviews */
.reviews-title{top:3180px;font-size:37px;color:var(--black);font-weight:600}
.avatar{position:absolute;width:118px;height:118px;border-radius:50%;border:4px solid var(--gold);
  background:radial-gradient(circle at 50% 40%,#8a5a36,#3b2414)}
.quote-mark{position:absolute;font-family:"Jost",sans-serif;font-weight:600;font-size:70px;line-height:70px;color:var(--gold)}
.review-text{position:absolute;width:290px;font-size:13.5px;line-height:22px;color:#222}
.review-name{position:absolute;font-family:"Jost",sans-serif;font-weight:600;font-size:14px;color:var(--black)}

/* footer */
.footer-dot{left:570px;top:3640px;width:60px;height:60px;border-radius:50%;background:var(--gold)}
.footer-brand{top:3744px;font-family:"Jost",sans-serif;font-size:20px;letter-spacing:1.5px;color:var(--gold)}
.footer-title{top:3785px;font-size:31px;line-height:34px;color:var(--gold);font-weight:500}
.footer-rule{left:94px;top:3964px;width:1014px;height:1px;background:#333}
.copyright{top:3983px;font-size:13px;color:var(--white)}
.to-top{left:1125px;top:3948px;width:34px;height:34px;border-radius:50%;background:var(--gold);
  display:flex;align-items:center;justify-content:center}
</style>
</head>
<body>
<div class="page">

  <!-- background waves -->
  <svg class="backdrop" viewBox="0 0 769 2576" preserveAspectRatio="none" aria-hidden="true">
    <defs>
      <linearGradient id="creamFade" x1="0" y1="0" x2="1" y2="1">
        <stop offset="0" stop-color="#e9c86c"/>
        <stop offset="0.45" stop-color="#f8ecc8"/>
        <stop offset="1" stop-color="#ffffff"/>
      </linearGradient>
      <linearGradient id="goldBand" x1="0" y1="0" x2="1" y2="0">
        <stop offset="0" stop-color="#c8901e"/>
        <stop offset="1" stop-color="#f0c94f"/>
      </linearGradient>
    </defs>
    <rect x="0" y="520" width="769" height="795" fill="url(#creamFade)"/>
    <path d="M0,10 C60,180 150,300 300,360 C420,410 600,418 769,430 L769,1000 C560,1060 400,1020 280,940 C110,870 30,720 0,545 Z" fill="#050505"/>
    <path d="M4,0 C40,150 140,290 280,345" fill="none" stroke="url(#goldBand)" stroke-width="4"/>
    <path d="M470,412 C600,398 700,410 769,440 L769,470 C680,440 590,420 470,412 Z" fill="url(#goldBand)"/>
    <path d="M0,1650 C250,1590 560,1590 769,1415 L769,1975 C600,1955 300,1960 0,2000 Z" fill="#050505"/>
    <path d="M0,1625 C200,1590 420,1585 620,1560 L620,1575 C420,1600 220,1610 0,1648 Z" fill="url(#goldBand)"/>
    <path d="M0,2170 C250,2250 550,2290 769,2370 L769,2576 L0,2576 Z" fill="#050505"/>
    <path d="M420,2265 C560,2290 680,2320 769,2345 L769,2375 C680,2340 560,2300 420,2265 Z" fill="url(#goldBand)"/>
  </svg>

  <!-- decorative flora placeholders -->
  <div class="abs" role="img" aria-label="Faint golden line-drawn leaves and blossom decoration" style="left:880px;top:120px;width:320px;height:560px;background:radial-gradient(ellipse at 60% 40%,rgba(233,196,110,0.18),rgba(255,255,255,0) 70%)"></div>
  <div class="abs" role="img" aria-label="Golden line-drawn magnolia decoration" style="left:0;top:760px;width:240px;height:220px;background:radial-gradient(ellipse,rgba(217,165,49,0.12),rgba(0,0,0,0) 70%)"></div>
  <div class="abs" role="img" aria-label="Golden line-drawn magnolia decoration" style="left:950px;top:1180px;width:250px;height:300px;background:radial-gradient(ellipse,rgba(217,165,49,0.12),rgba(0,0,0,0) 70%)"></div>
  <div class="abs" role="img" aria-label="Golden line-drawn magnolia decoration" style="left:990px;top:2420px;width:210px;height:240px;background:radial-gradient(ellipse,rgba(217,165,49,0.12),rgba(0,0,0,0) 70%)"></div>

  <!-- header -->
  <div class="brand">
    <div class="brand-dot"></div>
    <div class="brand-name">PLOOIFRIS</div>
  </div>
  <nav class="nav">
    <a class="active" style="left:0">Home</a>
    <a style="left:70px">Benefits</a>
    <a style="left:150px">About</a>
    <a style="left:220px">How It Works</a>
    <a style="left:335px">Customer Reviews</a>
    <a style="left:480px">FAQ</a>
  </nav>
  <div class="nav-tools">
    <span>En ▾</span>
    <svg width="18" height="18" viewBox="0 0 18 18" fill="none" stroke="#d9a531" stroke-width="1.4"><circle cx="9" cy="9" r="8"/><circle cx="9" cy="7" r="2.8"/><path d="M3.8,14.5 C5.5,11.5 12.5,11.5 14.2,14.5"/></svg>
    <svg width="16" height="18" viewBox="0 0 16 18" fill="none" stroke="#d9a531" stroke-width="1.4"><path d="M2,6 H14 L13,17 H3 Z"/><path d="M5,6 V4 a3,3 0 0 1 6,0 V6"/></svg>
  </div>

  <!-- hero -->
  <h1 class="abs center hero-title">Experience Luxury and<br>Sustainability in Every Wash</h1>
  <p class="abs center hero-sub">Discover Plooifris's premium laundry strips – where sophistication meets ecological consciousness.</p>
  <a class="btn" style="left:496px;top:245px;width:206px;height:31px">Try Now – Always Free Shipping!</a>
  <div class="box-art" role="img" aria-label="Product box of Plooistrips laundry strips in black, white and gold" style="left:403px;top:312px;width:362px;height:549px;background:linear-gradient(150deg,#f3f3f3 0%,#e6e6e6 30%,#111 45%,#000 100%);box-shadow:-30px 0 0 -4px #d9a531 inset"></div>

  <!-- benefits -->
  <h2 class="abs center section-title-gold" style="top:898px">Why Choose Plooifris Laundry Strips?</h2>

  <div class="benefit" style="left:203px;top:995px">
    <svg width="52" height="44" viewBox="0 0 52 44" fill="none" stroke="#d9a531" stroke-width="2"><path d="M26,42 C26,30 22,20 8,14 C8,26 16,32 26,32"/><path d="M26,32 C34,30 46,22 46,4 C34,6 28,14 26,26"/></svg>
    <h3>Eco-Friendly</h3>
    <p>100% biodegradable and<br>plastic-free.</p>
  </div>
  <div class="benefit" style="left:437px;top:995px">
    <svg width="52" height="44" viewBox="0 0 52 44" fill="none" stroke="#d9a531" stroke-width="2"><path d="M8,4 V40 M18,4 V40 M28,4 V40 M38,4 V40 M4,10 H44 M4,20 H44 M4,30 H44"/></svg>
    <h3>Suitable for All Fabrics</h3>
    <p>Safe for delicate laundry, whites,<br>colors, and blacks.</p>
  </div>
  <div class="benefit" style="left:710px;top:995px">
    <svg width="52" height="44" viewBox="0 0 52 44" fill="none" stroke="#d9a531" stroke-width="2"><path d="M26,2 C20,14 14,22 14,30 a12,12 0 0 0 24,0 C38,22 32,14 26,2 Z"/></svg>
    <h3>Compact and User-Friendly</h3>
    <p>No hassle with heavy bottles –<br>just tear, add, and enjoy.</p>
  </div>
  <div class="benefit" style="left:203px;top:1140px">
    <svg width="52" height="44" viewBox="0 0 52 44" fill="none" stroke="#d9a531" stroke-width="2"><circle cx="26" cy="22" r="5"/><circle cx="26" cy="10" r="7"/><circle cx="26" cy="34" r="7"/><circle cx="14" cy="22" r="7"/><circle cx="38" cy="22" r="7"/></svg>
    <h3>Long-Lasting Scent</h3>
    <p>A delightful fresh scent that<br>lingers for days.</p>
  </div>
  <div class="benefit" style="left:437px;top:1140px">
    <svg width="52" height="44" viewBox="0 0 52 44" fill="none" stroke="#d9a531" stroke-width="2.5"><circle cx="26" cy="22" r="19"/><path d="M17,22 L24,29 L38,12"/></svg>
    <h3>Hypoallergenic</h3>
    <p>Perfect for sensitive skin<br>and baby clothing.</p>
  </div>
  <div class="benefit" style="left:710px;top:1140px">
    <svg width="66" height="44" viewBox="0 0 66 44" fill="none" stroke="#d9a531" stroke-width="2"><path d="M4,6 H38 V34 H4 Z" stroke-dasharray="4 3"/><path d="M38,14 H52 L62,24 V34 H38"/><circle cx="16" cy="36" r="5"/><circle cx="50" cy="36" r="5"/></svg>
    <h3>Always Free Shipping</h3>
    <p>No minimum order<br>quantity required.</p>
  </div>

  <!-- product description -->
  <div class="box-art" role="img" aria-label="Product box of Plooistrips laundry strips on a cream background" style="left:231px;top:1511px;width:304px;height:468px;background:linear-gradient(150deg,#f3f3f3 0%,#e6e6e6 25%,#111 42%,#000 100%);box-shadow:-24px 0 0 -4px #d9a531 inset,0 20px 30px rgba(0,0,0,0.12)"></div>
  <h2 class="abs future-title">The Future of<br>Laundry Is Here</h2>
  <p class="abs future-text">Our Plooifris Laundry Strips combine innovation with sustainability. With just one strip per load, enjoy clean and beautifully scented laundry without burdening the environment. No plastic bottles, no waste – just pure washing power in a convenient strip.</p>

  <!-- how it works -->
  <h2 class="abs center steps-title">How to Use Laundry Strips</h2>
  <div class="step" style="left:142px;top:2131px"><div class="num">01</div><p>Tear off a laundry<br>strip.</p></div>
  <div class="step" style="left:376px;top:2131px"><div class="num">02</div><p>Place the strip directly in the<br>drum with your laundry.</p></div>
  <div class="step" style="left:605px;top:2131px"><div class="num">03</div><p>Start the washing machine and<br>let the strip do its work.</p></div>
  <div class="step" style="left:855px;top:2131px"><div class="num">04</div><p>Enjoy perfectly clean and<br>fresh-smelling clothes!</p></div>

  <svg class="abs" style="left:0;top:2225px" width="1200" height="150" viewBox="0 0 1200 150" fill="none" aria-hidden="true">
    <g stroke="#222" stroke-width="1.5">
      <path d="M239,10 V106 H540"/>
      <path d="M648,106 H945 V10"/>
      <path d="M470,10 V45 H710 V10"/>
      <path d="M590,45 V62"/>
    </g>
    <g fill="#d9a531"><circle cx="239" cy="10" r="2.5"/><circle cx="470" cy="10" r="2.5"/><circle cx="710" cy="10" r="2.5"/><circle cx="945" cy="10" r="2.5"/></g>
    <circle cx="594" cy="106" r="36" fill="#d9a531"/>
  </svg>
  <a class="btn" style="left:512px;top:2402px;width:176px;height:31px">Shop Now – From €14.95</a>

  <!-- faq -->
  <h2 class="abs center faq-title">Do You Have Any Questions?</h2>
  <div class="faq-item" style="top:2714px;height:100px;padding-top:18px">
    <div class="faq-q"><span>Are the strips suitable for people with sensitive skin?</span><span>+</span></div>
    <p class="faq-a">Yes, our strips are hypoallergenic and dermatologically tested, making them safe<br>for sensitive skin.</p>
  </div>
  <div class="faq-item" style="top:2821px;height:37px;padding-top:9px">
    <div class="faq-q"><span>How many washes does one pack contain?</span><span>–</span></div>
  </div>
  <div class="faq-item" style="top:2867px;height:37px;padding-top:9px">
    <div class="faq-q"><span>Do the strips work at low temperatures?</span><span>–</span></div>
  </div>
  <a class="btn" style="left:499px;top:2923px;width:200px;height:31px">Check Our FAQ for More Answers</a>

  <!-- reviews -->
  <h2 class="abs center reviews-title">What Our Customers Say</h2>
  <div class="avatar" role="img" aria-label="Portrait photo of customer Lieke" style="left:170px;top:3281px"></div>
  <div class="quote-mark" style="left:310px;top:3276px">“</div>
  <p class="review-text" style="left:312px;top:3322px">Since using Plooifris, my laundry feels fresher and more luxurious than ever.</p>
  <div class="review-name" style="left:312px;top:3374px">Lieke</div>

  <div class="avatar" role="img" aria-label="Portrait photo of customer Daan" style="left:605px;top:3281px"></div>
  <div class="quote-mark" style="left:742px;top:3276px">“</div>
  <p class="review-text" style="left:744px;top:3322px">Finally, an eco-friendly product that truly works and smells wonderful.</p>
  <div class="review-name" style="left:744px;top:3374px">Daan</div>

  <!-- footer -->
  <div class="abs footer-dot"></div>
  <div class="abs center footer-brand">PLOOIFRIS</div>
  <h2 class="abs center footer-title">Start Today with Eco-Friendly Laundry – No Plastic,<br>No Hassle. Just Fresh Laundry.</h2>
  <a class="btn" style="left:499px;top:3870px;width:200px;height:31px">Order Now – Make the Difference!</a>
  <div class="abs footer-rule"></div>
  <p class="abs center copyright">©Copyright 2024 | All Rights Reserved</p>
  <div class="abs to-top"><svg width="12" height="8" viewBox="0 0 12 8" fill="none" stroke="#fff" stroke-width="1.8"><path d="M1,7 L6,2 L11,7"/></svg></div>

</div>
</body>
</html>
```